Stationery Design For Specialist London law firm

We have merged two firms of London lawyers to create a new firm with a new name.

The new firms name is KR Holloway. We would like to include the description Solicitors and Advocates in the design.

We need a new design for our headed paper, business cards compliment slips etc.

The image we wish to project is fresh but not gimmicky - reliable and strong but not stuffy.

We have no strong views on font or colour this really is pretty much a blank page.

Our preference is for the name to be at the top of the page

Target Market(s)

Our clients who are individuals rather than corporate and other lawyers

Industry/Entity Type

Law Firm

Requirements
Should not have
• Legal images eg scales of justice etc

Obviously nothing childish or gimmicky

```html
<!DOCTYPE html>
<html lang="en">
<head>
<meta charset="utf-8">
<title>KR Holloway – Business Card</title>
<link rel="stylesheet" href="https://fonts.googleapis.com/css2?family=Exo+2:wght@200;300;400&display=swap">
<style>
  :root {
    --page: #ffffff;
    --card-light: #8cbfae;
    --card-mid: #7db3a1;
    --card-dark: #6fa693;
    --ink-light: #f4fbf8;
    --ink-dark: #2f3b38;
    --band: rgba(255, 255, 255, 0.28);
    --band-edge: rgba(255, 255, 255, 0.5);
    --shadow: rgba(0, 0, 0, 0.35);
  }

  * { margin: 0; padding: 0; box-sizing: border-box; }

  html, body {
    width: 1200px;
    height: 900px;
    overflow: hidden;
    background: var(--page);
  }

  .canvas {
    position: relative;
    width: 1200px;
    height: 900px;
    font-family: "Exo 2", "Helvetica Neue", Arial, sans-serif;
  }

  .card {
    position: absolute;
    overflow: hidden;
    background:
      radial-gradient(ellipse at 25% 30%, rgba(255,255,255,0.10), transparent 55%),
      radial-gradient(ellipse at 75% 80%, rgba(0,0,0,0.06), transparent 60%),
      linear-gradient(135deg, var(--card-light), var(--card-mid) 50%, var(--card-dark));
    box-shadow: 6px 10px 14px var(--shadow);
  }

  /* Front */
  .card--front {
    left: 130px;
    top: 78px;
    width: 520px;
    height: 311px;
  }

  .card__bands {
    position: absolute;
    inset: 0;
    width: 100%;
    height: 100%;
  }

  .front__name {
    position: absolute;
    left: 0;
    right: 0;
    top: 118px;
    text-align: center;
    font-weight: 200;
    font-size: 68px;
    line-height: 1;
    letter-spacing: -1px;
    color: var(--ink-light);
    text-transform: uppercase;
  }

  .front__tagline {
    position: absolute;
    left: 0;
    right: 0;
    top: 210px;
    text-align: center;
    font-weight: 300;
    font-size: 13px;
    letter-spacing: 0.2px;
    color: var(--ink-dark);
    text-transform: uppercase;
  }

  /* Back */
  .card--back {
    left: 540px;
    top: 440px;
    width: 550px;
    height: 329px;
  }

  .back__brand {
    position: absolute;
    right: 38px;
    top: 40px;
    text-align: center;
  }

  .back__name {
    font-weight: 300;
    font-size: 38px;
    line-height: 1;
    letter-spacing: -0.5px;
    color: var(--ink-dark);
    text-transform: uppercase;
  }

  .back__tagline {
    margin-top: 4px;
    font-weight: 300;
    font-size: 10px;
    color: var(--ink-dark);
    text-transform: uppercase;
  }

  .contact-list {
    position: absolute;
    left: 72px;
    top: 148px;
    list-style: none;
    font-weight: 300;
    font-size: 16px;
    line-height: 22.5px;
    color: var(--ink-light);
    text-transform: uppercase;
  }
</style>
</head>
<body>
<main class="canvas">

  <section class="card card--front" aria-label="Business card front">
    <svg class="card__bands" viewBox="0 0 520 311" aria-hidden="true">
      <polygon points="270,0 330,0 430,100 400,100" fill="var(--band)"/>
      <polygon points="340,0 410,0 520,110 520,180" fill="var(--band)"/>
      <line x1="340" y1="0" x2="520" y2="180" stroke="var(--band-edge)" stroke-width="1"/>
    </svg>
    <h1 class="front__name">KR Holloway</h1>
    <p class="front__tagline">Solicitors &amp; Advocates</p>
  </section>

  <section class="card card--back" aria-label="Business card back">
    <div class="back__brand">
      <p class="back__name">KR Holloway</p>
      <p class="back__tagline">Solicitors &amp; Advocates</p>
    </div>
    <ul class="contact-list">
      <li>Address</li>
      <li>Telephone</li>
      <li>Fax</li>
      <li>Email</li>
      <li>Website</li>
    </ul>
  </section>

</main>
</body>
</html>
```